Business Card Design Project

2 sided business card utilizing existing logo
- English on one side, Arabic on the other side (both English and Arabic text will be provided)
Same color scheme as logo
Information included will be: name, title, email, phone, address and website (www.dravelnix.com)
Updates

Target Market(s)

We are a Systems Integration Company

Industry/Entity Type

Business

Font styles to use
Serif
Sans Serif

Requirements
Should not have
• We prefer using the flat logo rather than one with shadow/3D effect

```html
<!DOCTYPE html>
<html lang="en">
<head>
<meta charset="utf-8">
<title>Dravelnix Systems – Business Card</title>
<link rel="stylesheet" href="https://fonts.googleapis.com/css2?family=Open+Sans:wght@400;600;700;800&display=swap">
<style>
  :root {
    --brand-red: #ee2129;
    --card-white: #ffffff;
    --ink: #1d1d1f;
    --pattern-pink: #fbe3e4;
    --backdrop: #ece8e2;
  }
  * { box-sizing: border-box; margin: 0; padding: 0; }
  html, body {
    width: 1200px; height: 846px; overflow: hidden;
    background: var(--backdrop);
    font-family: "Open Sans", Arial, sans-serif;
  }
  .sheet {
    position: relative; width: 1200px; height: 846px;
    display: flex; align-items: center; justify-content: center; gap: 48px;
  }
  .card {
    position: relative; width: 540px; height: 308px; overflow: hidden;
    box-shadow: 0 6px 18px rgba(0,0,0,.18);
  }
  .card-shapes { position: absolute; inset: 0; width: 100%; height: 100%; }

  /* Arabic side */
  .card--arabic { background: var(--card-white); }
  .card__pattern {
    position: absolute; inset: 0;
    background: linear-gradient(135deg, var(--pattern-pink) 0%, #fff4f4 55%, var(--pattern-pink) 100%);
  }
  .brand {
    position: absolute; left: 34px; bottom: 44px;
    color: var(--brand-red); font-weight: 800;
  }
  .brand__mark {
    width: 54px; height: 54px; background: var(--brand-red); margin-bottom: 22px;
  }
  .brand__name { font-size: 30px; letter-spacing: 9px; line-height: 1; }
  .brand__sub { font-size: 12px; letter-spacing: 10px; margin-top: 8px; line-height: 1; }

  .contact {
    position: absolute; color: var(--ink); font-size: 15px; line-height: 1.2;
  }
  .card--arabic .contact--name { right: 30px; top: 30px; text-align: right; }
  .card--arabic .contact--details { right: 30px; top: 118px; text-align: right; }
  .card--arabic .website {
    position: absolute; right: 30px; bottom: 26px;
    color: var(--brand-red); font-size: 14px; letter-spacing: 4px;
  }

  /* English side */
  .card--english { background: var(--brand-red); }
  .card--english .brand-head {
    position: absolute; right: 40px; top: 26px; text-align: right;
    color: var(--card-white); font-weight: 800;
  }
  .brand-head .brand__name { font-size: 44px; letter-spacing: 10px; }
  .brand-head .brand__sub { font-size: 14px; letter-spacing: 16px; margin-top: 10px; }
  .card--english .contact { font-weight: 600; }
  .card--english .contact--name { left: 42px; top: 136px; }
  .card--english .contact--details { right: 62px; top: 174px; text-align: right; }
  .card--english .website {
    position: absolute; left: 0; right: 0; bottom: 16px; text-align: center;
    color: var(--card-white); font-size: 15px; letter-spacing: 6px;
  }
</style>
</head>
<body>
<main class="sheet">

  <section class="card card--arabic" aria-label="Business card, Arabic side">
    <div class="card__pattern" role="img" aria-label="Faint repeating brand pattern in pale red"></div>
    <div class="brand">
      <div class="brand__mark"></div>
      <div class="brand__name">DRAVELNIX</div>
      <div class="brand__sub">SYSTEMS</div>
    </div>
    <p class="contact contact--name">ARABIC<br>Name:<br>Title</p>
    <p class="contact contact--details">email:<br>phone:<br>address</p>
    <p class="website">www.dravelnix.com</p>
  </section>

  <section class="card card--english" aria-label="Business card, English side">
    <svg class="card-shapes" viewBox="0 0 540 308" aria-hidden="true">
      <path d="M0 122 H470 L540 172 V226 L508 256 H0 Z" fill="var(--card-white)"/>
      <path d="M92 -10 Q40 40 38 122" fill="none" stroke="var(--card-white)" stroke-width="22"/>
    </svg>
    <div class="brand-head">
      <div class="brand__name">DRAVELNIX</div>
      <div class="brand__sub">SYSTEMS</div>
    </div>
    <p class="contact contact--name">Name:<br>Title</p>
    <p class="contact contact--details">email:<br>phone:<br>address</p>
    <p class="website">www.dravelnix.com</p>
  </section>

</main>
</body>
</html>
```